LoftRise Atlanta Event Space Flyer

- Create a "Z" fold flyer that captures the elegance of our event spaces and branding opportunities
- Include an a la carte menu located on what would be the back of the flyer
Details for the a la carte menu as as follows.
SPACE RENTAL
-- VIP lounge (Climate Controlled) ........... Hourly Rental.....Inquire
-- Veranda (Outdoors under the canopy)....Hourly Rental.....Inquire
-- Limited Furniture Rental...........................Per Event...........Inquire
BRANDING OPPORTUNITIES
-- Wheel Color Branding..............................Per Day..............Inquire
-- Globe Animation.......................................Per Hour............Inquire
Contact information to be included on the back page.
Loftrise Atlanta
427 Danberry Street NW
Atlanta GA, 30318
Phone number: 678.512.3746 Option 3
email: events@loftriseatlanta-example.com
***Pictures to be included in the flyer are attached as well as our logo.

```html
<!DOCTYPE html>
<html lang="en">
<head>
<meta charset="utf-8">
<title>LoftRise Atlanta – Event Space Flyer</title>
<link href="https://fonts.googleapis.com/css2?family=Oswald:wght@500;600;700&family=Roboto+Condensed:wght@400;700&display=swap" rel="stylesheet">
<style>
  :root {
    --backdrop: #6d6e70;
    --paper: #f4f5f7;
    --navy: #0d1f5c;
    --blue: #1a5cb0;
    --bright: #2c8fd8;
    --ink: #14286a;
    --line: #c9cdd8;
    --green-blur: #6f8a4e;
    --teal-blur: #4f7f86;
    --pink-blur: #d9b6dc;
  }
  * { box-sizing: border-box; margin: 0; padding: 0; }
  html, body { width: 1200px; height: 1000px; overflow: hidden; }
  body {
    background: var(--backdrop);
    font-family: "Roboto Condensed", "Arial Narrow", sans-serif;
    color: var(--ink);
  }
  .flyer {
    position: absolute; left: 60px; top: 110px;
    width: 1080px; height: 780px;
    display: flex;
    box-shadow: 0 18px 40px rgba(0,0,0,.35);
  }
  .panel {
    position: relative; width: 360px; height: 780px;
    background: var(--paper); overflow: hidden;
  }
  .panel + .panel { border-left: 1px solid #dcdfe5; }
  .photo-wash {
    position: absolute; left: 0; right: 0; bottom: 0; height: 62%;
    background:
      radial-gradient(ellipse at 30% 60%, rgba(111,138,78,.85), transparent 60%),
      radial-gradient(ellipse at 80% 40%, rgba(79,127,134,.7), transparent 60%),
      linear-gradient(to bottom, rgba(244,245,247,0) 0%, #8fa78a 40%, #5d7a52 100%);
  }
  .cover .photo-wash {
    background:
      radial-gradient(ellipse at 85% 85%, rgba(217,182,220,.9), transparent 55%),
      radial-gradient(ellipse at 30% 50%, rgba(111,138,78,.85), transparent 60%),
      linear-gradient(to bottom, rgba(244,245,247,0) 0%, #9cae86 40%, #6b8a5a 100%);
  }
  .pill {
    display: inline-block;
    background: linear-gradient(90deg, var(--navy), var(--blue) 60%, var(--bright));
    color: #fff; font-family: "Oswald", sans-serif; font-weight: 600;
    text-transform: uppercase; letter-spacing: .5px;
    border-radius: 12px; border: 2px solid #fff;
  }
  /* menu panel */
  .menu { padding: 40px 26px 0; }
  .menu-title { position: relative; font-size: 34px; padding: 8px 24px; }
  .section-heading {
    position: relative; font-family: "Oswald", sans-serif; font-weight: 600;
    font-size: 26px; color: var(--navy); text-transform: uppercase;
    text-align: center; margin: 22px 0 12px;
  }
  .price-table {
    position: relative; width: 100%; border-collapse: collapse;
    background: rgba(255,255,255,.72); border-radius: 14px; overflow: hidden;
    font-weight: 700; font-size: 14px; text-transform: uppercase; color: var(--navy);
  }
  .price-table td {
    padding: 12px 8px; border: 1px solid var(--line); vertical-align: middle; line-height: 1.2;
  }
  .price-table td:first-child { width: 44%; }
  .price-table td:last-child { text-align: center; font-family: "Oswald", sans-serif; font-weight: 500; font-size: 16px; }
  /* contact panel */
  .contact { padding-top: 40px; }
  .contact-bar { position: relative; display: block; margin: 0 24px; font-size: 24px; padding: 8px 0; text-align: center; }
  .contact-list { position: relative; list-style: none; margin: 40px 28px 0; }
  .contact-list li { display: flex; align-items: center; gap: 16px; margin-bottom: 36px; font-size: 17px; font-weight: 700; color: var(--navy); line-height: 1.35; }
  .icon-box {
    flex: none; width: 46px; height: 46px; border-radius: 8px;
    background: linear-gradient(135deg, var(--navy), var(--bright));
    display: flex; align-items: center; justify-content: center;
  }
  .contact-list .email { font-size: 14.5px; word-break: break-all; }
  /* cover panel */
  .brand { position: relative; display: flex; align-items: center; gap: 12px; margin: 48px 0 0 34px; }
  .brand-dot { width: 22px; height: 22px; border-radius: 50%; background: var(--navy); }
  .brand-name { font-family: "Oswald", sans-serif; font-weight: 700; font-size: 30px; color: var(--navy); text-transform: uppercase; }
  .venue-collage {
    position: absolute; left: 70px; top: 170px; width: 300px; height: 330px;
    clip-path: polygon(45% 0, 100% 0, 100% 70%, 70% 100%, 25% 100%, 0 75%, 20% 45%);
    background: linear-gradient(160deg, #f2e4de 0%, #dfe3ea 35%, #c4ccd8 60%, #9b3144 78%, #d7dbe3 100%);
  }
  .cover-cta { position: absolute; left: 24px; bottom: 70px; display: flex; flex-direction: column; gap: 18px; }
  .cover-cta .pill { font-size: 22px; padding: 10px 18px; text-align: center; }
  .cover-cta .pill.large { font-size: 25px; }
</style>
</head>
<body>
<main class="flyer">
  <section class="panel menu">
    <div class="photo-wash" role="img" aria-label="Soft blurred photo of the venue terrace with greenery"></div>
    <h1 class="pill menu-title">A La Carte Menu</h1>
    <h2 class="section-heading">Space Rental</h2>
    <table class="price-table">
      <tr><td>VIP Lounge (Climate Controlled)</td><td>Hourly Rental</td><td>Inquire</td></tr>
      <tr><td>Veranda (Outdoors under the canopy)</td><td>Hourly Rental</td><td>Inquire</td></tr>
      <tr><td>Limited Furniture Rental</td><td>Per Event</td><td>Inquire</td></tr>
    </table>
    <h2 class="section-heading">Branding Opportunities</h2>
    <table class="price-table">
      <tr><td>Wheel Color Branding</td><td>Per Day</td><td>Inquire</td></tr>
      <tr><td>Globe Animation</td><td>Per Hour</td><td>Inquire</td></tr>
    </table>
  </section>

  <section class="panel contact">
    <div class="photo-wash" role="img" aria-label="Soft blurred photo of the illuminated venue at dusk"></div>
    <h2 class="pill contact-bar">Contact Us</h2>
    <ul class="contact-list">
      <li>
        <span class="icon-box"><svg width="22" height="26" viewBox="0 0 22 26"><path d="M11 1a9 9 0 0 0-9 9c0 7 9 15 9 15s9-8 9-15a9 9 0 0 0-9-9z" fill="#fff"/><circle cx="11" cy="10" r="3.5" fill="#1a5cb0"/></svg></span>
        <span>Loftrise Atlanta<br>427 Danberry Street NW<br>Atlanta GA, 30318</span>
      </li>
      <li>
        <span class="icon-box"><svg width="24" height="24" viewBox="0 0 24 24"><path d="M6 2l4 5-2 3c1 2.5 3.5 5 6 6l3-2 5 4-2 4C10 22 2 14 2 4z" fill="#fff"/></svg></span>
        <span>678.512.3746 Option 3</span>
      </li>
      <li>
        <span class="icon-box"><svg width="26" height="20" viewBox="0 0 26 20"><rect x="1" y="1" width="24" height="18" rx="2" fill="#fff"/><path d="M2 3l11 8 11-8" fill="none" stroke="#1a5cb0" stroke-width="2"/></svg></span>
        <span class="email">events@loftriseatlanta-example.com</span>
      </li>
    </ul>
  </section>

  <section class="panel cover">
    <div class="photo-wash" role="img" aria-label="Soft blurred photo of the venue grounds with greenery and evening light"></div>
    <div class="brand"><span class="brand-dot"></span><span class="brand-name">LoftRise Atlanta</span></div>
    <div class="venue-collage" role="img" aria-label="Collage of the VIP lounge interior with white tufted walls, glass table and red bar stools"></div>
    <div class="cover-cta">
      <span class="pill">Looking for an event space?</span>
      <span class="pill large">Check out our VIP space!</span>
    </div>
  </section>
</main>
</body>
</html>
```